Webdesign für Raumwerkplanung
Zielgruppe
Die Firma heißt: rwp Raumwerkplanung GmbH und beschäftigt sich mit individueller Raumgestaltung und Friseurtechnik für Friseurgeschäfte
Aufgabenstellung
Achtung: es gibt zwei Logos, die beide eingearbeitet werden sollen. Der Fokus liegt jedoch auf rwp_neu.jpg - siehe Dateiupload + Slogan 'Richten Sie sich darauf ein, dass wir Sie nicht einfach einrichten' Dabei soll das 'einfach' auf dem Kopf stehen und in Pink dargestellt werden.
- Slider ja
- Farbe Pink (davon nicht zu viel) und Grauschattierungen
- Schriftart nicht zu verschnörkelt
- die 4 Hauptlieferanten sollten mit Logo dargestellt werden ( Borvani, glowhaven, Varelm, krelf)- siehe Anlage

```html
<!DOCTYPE html>
<html lang="de">
<head>
<meta charset="utf-8">
<title>rwp Raumwerkplanung GmbH</title>
<link rel="stylesheet" href="https://fonts.googleapis.com/css2?family=Open+Sans:wght@400;600;700&display=swap">
<style>
  :root {
    --pink: #e3179d;
    --text: #555a5e;
    --text-dark: #44494d;
    --panel: #f2f0f1;
    --white: #ffffff;
    --dot: #ebe9ea;
    --link: #8b8f92;
  }
  * { box-sizing: border-box; margin: 0; padding: 0; }
  html, body { width: 779px; height: 1200px; overflow: hidden; background: var(--white); }
  body { position: relative; font-family: 'Open Sans', Arial, sans-serif; color: var(--text); }
  .abs { position: absolute; }

  /* Header */
  .slogan { right: 49px; top: 10px; font-size: 8.5px; font-weight: 700; color: var(--text-dark); white-space: nowrap; }
  .slogan .flip { display: inline-block; transform: rotate(180deg); color: var(--pink); margin: 0 3px; }
  .brand { left: 50px; top: 28px; display: flex; align-items: center; gap: 6px; }
  .brand-mark { width: 10px; height: 10px; background: var(--pink); }
  .brand-name { font-size: 34px; font-weight: 700; color: var(--pink); line-height: 1; letter-spacing: 1px; }
  .nav a { position: absolute; top: 49px; font-size: 11px; color: var(--text); text-decoration: none; white-space: nowrap; }
  .nav a.active { color: var(--pink); }

  /* Hero */
  .hero { left: 0; top: 80px; width: 779px; height: 241px; background: var(--panel); }
  .hero-photo { left: 0; top: 80px; width: 361px; height: 241px; background: linear-gradient(135deg, #b9a79a 0%, #4e4a48 45%, #3a3838 70%, #8a7a6c 100%); }
  .hero-title { left: 406px; top: 111px; font-size: 23px; line-height: 26px; font-weight: 400; color: var(--pink); }
  .hero-lead { left: 406px; top: 198px; font-size: 11px; font-weight: 700; color: var(--text-dark); }
  .hero-list { left: 406px; top: 216px; list-style: none; font-size: 11px; line-height: 19px; }
  .hero-list li::before { content: "• "; color: var(--pink); }

  /* Partners */
  .partner { top: 384px; transform: translateX(-50%); font-size: 22px; font-weight: 700; color: #1f1f1f; display: flex; align-items: center; gap: 6px; white-space: nowrap; }
  .partner .sq { width: 10px; height: 10px; background: #1f1f1f; }

  /* References */
  .refs { left: 0; top: 469px; width: 418px; height: 241px; background: var(--panel); }
  .refs-photo { left: 418px; top: 469px; width: 361px; height: 241px; background: linear-gradient(170deg, #f1efee 0%, #d8d2cc 40%, #9a5a35 70%, #6b3c22 100%); }
  .section-title { font-size: 23px; font-weight: 400; color: var(--pink); line-height: 28px; }
  .copy { font-size: 11.2px; line-height: 15px; }
  .btn { display: flex; align-items: center; justify-content: center; background: var(--pink); color: var(--white); font-size: 11px; font-weight: 700; height: 26px; }

  /* Slider */
  .slide-photo { left: 97px; top: 756px; width: 286px; height: 192px; background: linear-gradient(180deg, #5f6b3a 0%, #8c8a4a 45%, #9aa55a 70%, #6f7a3e 100%); }
  .slide-title { left: 415px; top: 763px; font-size: 24px; line-height: 26px; font-weight: 400; color: var(--pink); }
  .dots { left: 344px; top: 981px; display: flex; align-items: center; gap: 7px; }
  .dots span { width: 12px; height: 12px; border-radius: 50%; background: var(--dot); }
  .dots span.on { width: 16px; height: 16px; background: var(--pink); }

  /* Footer */
  .footer { left: 0; top: 1033px; width: 779px; height: 167px; background: var(--panel); }
  .footer-col { top: 1051px; font-size: 11px; line-height: 19px; }
  .footer-col strong { color: var(--text-dark); font-weight: 700; }
  .footer-link { top: 1170px; font-size: 10px; color: var(--link); text-decoration: underline; }
  .seal { left: 650px; top: 1113px; display: flex; align-items: center; gap: 5px; font-size: 14px; font-weight: 700; color: #111; }
  .seal .sq { width: 10px; height: 10px; background: #111; }
</style>
</head>
<body>

<header>
  <p class="abs slogan">Richten Sie sich darauf ein, dass wir Sie nicht<span class="flip">einfach</span>einrichten</p>
  <div class="abs brand"><span class="brand-mark"></span><span class="brand-name">rwp</span></div>
  <nav class="nav">
    <a class="active" style="left:256px">Home</a>
    <a style="left:322px">Was wir tun</a>
    <a style="left:419px">Referenzen</a>
    <a style="left:522px">Aktuelle Meldungen</a>
    <a style="left:669px">Vorstellung</a>
  </nav>
</header>

<section>
  <div class="abs hero"></div>
  <div class="abs hero-photo" role="img" aria-label="Hände mit Materialmustern, Farbkarten und Tablet mit Raumplanung auf dunklem Teppich"></div>
  <h1 class="abs hero-title">Seit 1990 Ihr Partner<br>für Qualität, Funktionalität<br>und Service</h1>
  <p class="abs hero-lead">Wir planen, liefern und montieren Einrichtungen für:</p>
  <ul class="abs hero-list">
    <li>Friseur / Kosmetik / Fußpflege / Nagelpflege</li>
    <li>Arztpraxen / Empfangs- und Wartebereiche</li>
    <li>Gastronomie / Restaurant / Bistro / Imbiss</li>
    <li>Private Wohnbereiche / individueller Möbelbau</li>
  </ul>
</section>

<section aria-label="Hauptlieferanten">
  <div class="abs partner" style="left:113px"><span class="sq"></span>glowhaven</div>
  <div class="abs partner" style="left:283px">Borvani</div>
  <div class="abs partner" style="left:453px">krelf</div>
  <div class="abs partner" style="left:641px">Varelm</div>
</section>

<section>
  <div class="abs refs"></div>
  <div class="abs refs-photo" role="img" aria-label="Heller Friseursalon mit Spiegeln, schwarzen Stühlen und glänzendem Holzboden"></div>
  <h2 class="abs section-title" style="left:46px;top:497px">Unsere Referenzen</h2>
  <p class="abs copy" style="left:46px;top:536px;width:320px">Wir bieten Ihnen individuelle Einrichtungskonzepte, ausgefallenes Design und einen umfassenden Service für unsere Produkte.</p>
  <p class="abs copy" style="left:46px;top:605px;width:320px">Eine große Vielfalt an Materialien und Farben geben Ihrer Einrichtung eine einzigartige und individuelle Note.</p>
  <a class="abs btn" style="left:46px;top:650px;width:146px">Referenzen</a>
</section>

<section aria-label="Slider">
  <svg class="abs" style="left:40px;top:833px" width="28" height="58" viewBox="0 0 28 58"><polyline points="26,2 3,29 26,56" fill="none" stroke="var(--pink)" stroke-width="4" stroke-linecap="round" stroke-linejoin="round"/></svg>
  <svg class="abs" style="left:719px;top:833px" width="28" height="58" viewBox="0 0 28 58"><polyline points="2,2 25,29 2,56" fill="none" stroke="var(--pink)" stroke-width="4" stroke-linecap="round" stroke-linejoin="round"/></svg>
  <div class="abs slide-photo" role="img" aria-label="Salonstühle und ovaler Spiegel im herbstlichen Park"></div>
  <h2 class="abs slide-title">Aktueller Trend:<br>Naturfarben, Licht und<br>Design.</h2>
  <p class="abs copy" style="left:415px;top:853px;width:240px">Der Salon zwischen Impressionismus Style und dem Wunsch nach Design</p>
  <a class="abs btn" style="left:415px;top:899px;width:146px">Aktuelle Meldungen</a>
  <div class="abs dots"><span></span><span class="on"></span><span></span><span></span><span></span></div>
</section>

<footer>
  <div class="abs footer"></div>
  <div class="abs footer-col" style="left:45px">
    <strong>rwp Raumwerkplanung GmbH</strong><br>
    Tel 0341 550 21 80<br>
    Fax 0341 550 21 81<br>
    Mail&nbsp; info[at]rwp-mittelstadt.de
  </div>
  <div class="abs footer-col" style="left:312px">
    <strong>Ausstellungsraum</strong><br>
    Lindenhofer Straße 14<br>
    04217 Mittelstadt<br>
    Mo bis Do von 8-16 Uhr<br>
    Fr von 8-14 Uhr
  </div>
  <div class="abs seal"><span class="sq"></span>Werkprofil</div>
  <a class="abs footer-link" style="left:45px">Impressum</a>
  <a class="abs footer-link" style="left:146px">Datenschutzerklärung</a>
  <a class="abs footer-link" style="left:310px">Haftungsausschuss</a>
</footer>

</body>
</html>
```